VELMOTIK Amazing Business Cards Challenge

Velmoti is a new technology company that will provide engineering and manufacturing services in the electric vehicle industry.

We are looking at a new business card that will support our orientation in providing advanced, innovative solutions. The business card will be lean and present the only information required to be more efficient.

Target Market(s)

Fleet operators, private commercial vehicle operators, delivery companies.

Industry/Entity Type

Business

Contact Information for Business Card

Use the logo and its colors, use a white background.

Font styles to use
Sans Serif

Colors
0455a3
ffffff
9bcb3c

Requirements
Must have
• Velmotik Logo
• All informations in the DOC file = 3 different cards.
• White background
Nice to have
• Icons for email, phone and web address.
• Cute design and strong identity.
Should not have
• Bleeds

```html
<!DOCTYPE html>
<html lang="en">
<head>
<meta charset="utf-8">
<title>Velmotik Business Cards</title>
<link href="https://fonts.googleapis.com/css2?family=Open+Sans:wght@400;600;700&display=swap" rel="stylesheet">
<style>
  :root {
    --stage: #eef0f2;
    --navy: #0455a3;
    --green: #9bcb3c;
    --white: #ffffff;
    --ink: #2b2b2b;
    --grey-text: #5f6368;
  }
  * { box-sizing: border-box; margin: 0; padding: 0; }
  html, body {
    width: 1200px; height: 1200px; overflow: hidden;
    background: var(--stage);
    font-family: "Open Sans", Arial, sans-serif;
  }
  .sheet {
    width: 1200px; height: 1200px;
    display: grid;
    grid-template-columns: 540px 540px;
    grid-template-rows: 309px 309px;
    gap: 48px 40px;
    place-content: center;
  }
  .card {
    position: relative; width: 540px; height: 309px; overflow: hidden;
    background: var(--white);
    box-shadow: 0 6px 22px rgba(0,0,0,0.10);
  }
  /* Front */
  .card--front { display: flex; align-items: center; justify-content: center; }
  .front-brand { display: flex; flex-direction: column; align-items: center; gap: 14px; }
  .front-brand__mark { width: 54px; height: 54px; background: var(--navy); }
  .front-brand__name {
    color: var(--navy); font-weight: 400; font-size: 58px; letter-spacing: 1px; line-height: 1;
  }
  .front-strip { position: absolute; left: 0; bottom: 0; width: 540px; height: 10px; background: var(--green); }
  /* Back */
  .person { position: absolute; left: 30px; top: 30px; display: flex; gap: 12px; }
  .person__accent { width: 10px; height: 36px; background: var(--navy); flex: none; }
  .person__name { font-size: 17px; font-weight: 600; color: var(--ink); line-height: 1.2; white-space: nowrap; }
  .person__title { font-size: 11px; color: var(--green); font-weight: 700; margin-top: 2px; }
  .contact {
    position: absolute; left: 52px; top: 118px;
    font-size: 11px; line-height: 1.6; color: var(--grey-text);
  }
  .contact__row { display: flex; align-items: center; gap: 6px; white-space: nowrap; }
  .contact__row svg { width: 10px; height: 10px; fill: var(--navy); flex: none; }
  .back-brand {
    position: absolute; right: 36px; top: 128px; display: flex; align-items: center; gap: 10px;
  }
  .back-brand__mark { width: 26px; height: 26px; background: var(--navy); }
  .back-brand__name { font-size: 28px; font-weight: 400; color: var(--navy); letter-spacing: 0.5px; line-height: 1; }
  .footer-band { position: absolute; left: 0; bottom: 0; width: 540px; height: 34px; display: block; }
</style>
</head>
<body>
<main class="sheet">
  <section class="card card--front" aria-label="Card front">
    <div class="front-brand">
      <span class="front-brand__mark"></span>
      <span class="front-brand__name">Velmotik</span>
    </div>
    <span class="front-strip"></span>
  </section>

  <section class="card card--back" aria-label="Card back, president">
    <div class="person">
      <span class="person__accent"></span>
      <div>
        <p class="person__name">Étienne Marchand, P.Eng, MASc</p>
        <p class="person__title">President | CEO</p>
      </div>
    </div>
    <div class="contact">
      <p class="contact__row">1180 Rue des Érables, Suite 400</p>
      <p class="contact__row">Montreal (Quebec) Canada H3B 2K7</p>
      <p class="contact__row"><svg viewBox="0 0 16 16" aria-hidden="true"><path d="M3.5 1l3 3-2 2a9 9 0 0 0 5.5 5.5l2-2 3 3-2 2.5C7 15 1 9 1 3.5z"/></svg>T: +1.514.555.0148</p>
      <p class="contact__row"><svg viewBox="0 0 16 16" aria-hidden="true"><path d="M1 3h14v10H1zM2 4l6 5 6-5v1L8 10 2 5z" fill-rule="evenodd"/></svg>E: emarchand@velmotik.com</p>
      <p class="contact__row"><svg viewBox="0 0 16 16" aria-hidden="true"><circle cx="8" cy="8" r="7"/></svg>www.velmotik.com</p>
    </div>
    <div class="back-brand"><span class="back-brand__mark"></span><span class="back-brand__name">Velmotik</span></div>
    <svg class="footer-band" viewBox="0 0 540 34" aria-hidden="true">
      <rect x="0" y="23" width="162" height="11" fill="#9bcb3c"/>
      <polygon points="162,12 540,12 540,34 151,34" fill="#0455a3"/>
    </svg>
  </section>

  <section class="card card--back" aria-label="Card back, engineering">
    <div class="person">
      <span class="person__accent"></span>
      <div>
        <p class="person__name">Nadia Fortier, P.Eng</p>
        <p class="person__title">VP Engineering</p>
      </div>
    </div>
    <div class="contact">
      <p class="contact__row">1180 Rue des Érables, Suite 400</p>
      <p class="contact__row">Montreal (Quebec) Canada H3B 2K7</p>
      <p class="contact__row"><svg viewBox="0 0 16 16" aria-hidden="true"><path d="M3.5 1l3 3-2 2a9 9 0 0 0 5.5 5.5l2-2 3 3-2 2.5C7 15 1 9 1 3.5z"/></svg>T: +1.514.555.0162</p>
      <p class="contact__row"><svg viewBox="0 0 16 16" aria-hidden="true"><path d="M1 3h14v10H1zM2 4l6 5 6-5v1L8 10 2 5z" fill-rule="evenodd"/></svg>E: nfortier@velmotik.com</p>
      <p class="contact__row"><svg viewBox="0 0 16 16" aria-hidden="true"><circle cx="8" cy="8" r="7"/></svg>www.velmotik.com</p>
    </div>
    <div class="back-brand"><span class="back-brand__mark"></span><span class="back-brand__name">Velmotik</span></div>
    <svg class="footer-band" viewBox="0 0 540 34" aria-hidden="true">
      <rect x="0" y="23" width="162" height="11" fill="#9bcb3c"/>
      <polygon points="162,12 540,12 540,34 151,34" fill="#0455a3"/>
    </svg>
  </section>

  <section class="card card--back" aria-label="Card back, operations">
    <div class="person">
      <span class="person__accent"></span>
      <div>
        <p class="person__name">Marc-André Leduc</p>
        <p class="person__title">Director of Operations</p>
      </div>
    </div>
    <div class="contact">
      <p class="contact__row">1180 Rue des Érables, Suite 400</p>
      <p class="contact__row">Montreal (Quebec) Canada H3B 2K7</p>
      <p class="contact__row"><svg viewBox="0 0 16 16" aria-hidden="true"><path d="M3.5 1l3 3-2 2a9 9 0 0 0 5.5 5.5l2-2 3 3-2 2.5C7 15 1 9 1 3.5z"/></svg>T: +1.514.555.0177</p>
      <p class="contact__row"><svg viewBox="0 0 16 16" aria-hidden="true"><path d="M1 3h14v10H1zM2 4l6 5 6-5v1L8 10 2 5z" fill-rule="evenodd"/></svg>E: maleduc@velmotik.com</p>
      <p class="contact__row"><svg viewBox="0 0 16 16" aria-hidden="true"><circle cx="8" cy="8" r="7"/></svg>www.velmotik.com</p>
    </div>
    <div class="back-brand"><span class="back-brand__mark"></span><span class="back-brand__name">Velmotik</span></div>
    <svg class="footer-band" viewBox="0 0 540 34" aria-hidden="true">
      <rect x="0" y="23" width="162" height="11" fill="#9bcb3c"/>
      <polygon points="162,12 540,12 540,34 151,34" fill="#0455a3"/>
    </svg>
  </section>
</main>
</body>
</html>
```